Banner 34"x81"

This is for a Pull Up Banner
I am supplying a sample of my logo and some of my art work for you to incorporate into an upright banner.
Please business name:LuellaRo OpenHarbor Psychotherapy
phone number: 583-214-9067 NOT THE ONE ON THE BUSINESS CARD

```html
<!DOCTYPE html>
<html lang="en">
<head>
<meta charset="UTF-8">
<title>LuellaRo OpenHarbor Psychotherapy – Pull Up Banner</title>
<link href="https://fonts.googleapis.com/css2?family=Nunito:wght@300;400;600;700&display=swap" rel="stylesheet">
<style>
  :root{
    --stage:#2128c6;
    --navy-top:#0e1a3a;
    --navy-mid:#0a1228;
    --navy-deep:#05070f;
    --gold-light:#f3d23a;
    --gold-dark:#c99a12;
    --yellow-text:#f5e84a;
    --white:#ffffff;
    --logo-blue:#2a62b0;
  }
  *{margin:0;padding:0;box-sizing:border-box}
  html,body{width:1200px;height:1050px;overflow:hidden}
  body{background:var(--stage);font-family:'Nunito',sans-serif;position:relative}

  .banner{
    position:absolute;left:390px;top:28px;width:421px;height:993px;overflow:hidden;
    background:linear-gradient(180deg,var(--navy-top) 0%,var(--navy-mid) 55%,var(--navy-deep) 100%);
  }
  .helix-backdrop{
    position:absolute;left:90px;top:40px;width:300px;height:860px;
    background:radial-gradient(ellipse at 60% 45%,rgba(70,90,140,.35) 0%,rgba(30,40,70,.15) 45%,rgba(0,0,0,0) 70%);
  }
  .gold-splash{position:absolute}
  .gold-splash.top{left:0;top:0;width:320px;height:205px}
  .gold-splash.bottom{right:0;bottom:0;width:195px;height:115px}

  .brand-tile{
    position:absolute;left:141px;top:166px;width:134px;height:108px;background:var(--logo-blue);
    display:flex;align-items:center;justify-content:center;
    color:var(--white);font-weight:600;font-size:24px;
  }
  .owner-name{
    position:absolute;left:0;width:100%;top:304px;text-align:center;
    color:var(--yellow-text);font-weight:400;font-size:60px;line-height:1;
  }
  .portrait{
    position:absolute;left:54px;top:399px;width:149px;height:220px;border:3px solid var(--white);
    background:linear-gradient(180deg,#3a2620 0%,#24160f 40%,#1f4fb8 70%,#5b5f6a 100%);
  }
  .brand-mark{
    position:absolute;left:212px;top:399px;width:160px;height:220px;
    display:flex;align-items:center;justify-content:center;
    color:var(--white);font-weight:700;font-size:32px;
  }
  .practice-name{
    position:absolute;left:54px;width:313px;top:638px;text-align:center;
    color:var(--yellow-text);font-weight:400;font-size:46px;line-height:1;
  }
  .practice-type{
    position:absolute;left:54px;width:313px;top:690px;text-align:center;
    color:var(--yellow-text);font-size:19px;letter-spacing:9.4px;line-height:1;padding-left:9px;
  }
  .phone-row{position:absolute;left:58px;top:735px;display:flex;align-items:center;gap:12px}
  .phone-row svg{width:24px;height:40px}
  .phone-number{color:var(--white);font-size:40px;font-weight:400;line-height:1}

  .contact-list{position:absolute;left:58px;top:802px;list-style:none}
  .contact-list li{display:flex;align-items:center;gap:9px;height:27px;margin-bottom:13px;color:var(--white);font-size:15px;font-weight:300}
  .contact-dot{width:27px;height:27px;border-radius:50%;background:var(--white);flex:none;display:flex;align-items:center;justify-content:center}
</style>
</head>
<body>
  <main class="banner">
    <div class="helix-backdrop" role="img" aria-label="Soft dark DNA helix artwork in the background"></div>

    <svg class="gold-splash top" viewBox="0 0 320 205" role="img" aria-label="Gold foil splash corner">
      <defs>
        <linearGradient id="goldTop" x1="0" y1="0" x2="1" y2="1">
          <stop offset="0" stop-color="var(--gold-light)"/>
          <stop offset="1" stop-color="var(--gold-dark)"/>
        </linearGradient>
      </defs>
      <path d="M0 0H296L310 60L290 78L240 100L205 70L175 95L120 120L80 140L70 170L30 185L0 205Z" fill="url(#goldTop)"/>
    </svg>

    <svg class="gold-splash bottom" viewBox="0 0 195 115" role="img" aria-label="Gold foil splash corner">
      <defs>
        <linearGradient id="goldBottom" x1="0" y1="0" x2="1" y2="1">
          <stop offset="0" stop-color="var(--gold-light)"/>
          <stop offset="1" stop-color="var(--gold-dark)"/>
        </linearGradient>
      </defs>
      <path d="M195 10V115H0L18 80L40 55L90 35L130 20L140 0L150 22L175 18L185 12Z" fill="url(#goldBottom)"/>
    </svg>

    <div class="brand-tile">LuellaRo</div>

    <h1 class="owner-name">LuellaRo</h1>

    <div class="portrait" role="img" aria-label="Portrait photo of the therapist seated in a leather chair"></div>
    <div class="brand-mark">LuellaRo</div>

    <h2 class="practice-name">OpenHarbor</h2>
    <p class="practice-type">PSYCHOTHERAPY</p>

    <div class="phone-row">
      <svg viewBox="0 0 24 40" aria-hidden="true">
        <rect x="2" y="1.5" width="20" height="37" rx="3" fill="none" stroke="var(--white)" stroke-width="2.5"/>
        <line x1="2" y1="7" x2="22" y2="7" stroke="var(--white)" stroke-width="2"/>
        <line x1="2" y1="32" x2="22" y2="32" stroke="var(--white)" stroke-width="2"/>
        <circle cx="12" cy="35.3" r="1.4" fill="var(--white)"/>
        <path d="M8 13c0 6 3 10 8 12l1.5-2.5-2.5-2-1.5 1c-1.5-1-2.5-2.5-3-4l1-1.5-2-2.5Z" fill="var(--white)"/>
      </svg>
      <span class="phone-number">583-214-9067</span>
    </div>

    <ul class="contact-list">
      <li><span class="contact-dot">
        <svg width="15" height="11" viewBox="0 0 15 11" aria-hidden="true"><rect x="0.5" y="0.5" width="14" height="10" rx="1" fill="var(--logo-blue)"/><path d="M1 1l6.5 5L14 1" fill="none" stroke="var(--white)" stroke-width="1.2"/></svg>
      </span>hello@openharborcare.com</li>
      <li><span class="contact-dot"></span>@LuellaOpenHarbor</li>
      <li><span class="contact-dot"></span>@LuellaHarbor</li>
    </ul>
  </main>
</body>
</html>
```